Holistic Therapy (aromatherapy, massage, reflexology, life coaching, soul healing, aura reading)

I work for myself as a holistic therapist doing: aromatherapy massage, massage, reflexology, abdominal-sacral massage, life coaching, soul healing, aura readings. I want a business card that doesn't focus on any one of these( so not just feet or a massage couch,but rather a card that creates the feeling of wholeness, healing, health and which can encompass all my therapies - e.g. green or purple are colours I like (especially green, or maybe green on back and purple on front). It's going to be called Rosa Elwin Therapies. I don't want to list all my therapies on the card in case I add others later.). At some point I will create a website but in this instance I just want to get some cards printed to get 'out there' while I design my website.
Updates

Hi, thanks for all your designs. Can you find a way to include the therapies that I offer within the card, either on the front or back…the therapies I offer are: aromatherapy massage, reflexology, swedish body massage, abdominal-sacral massage, nutrition, soul healing, aura readings. (Maybe have them with a bullet point before each?) I am not sure whether they should be on the front of the card or the back or whether having them would spoil the card but it occurred to me that just having rosa elwin therapies doesn't tell people what therapies I offer, hence the new idea to list them somehow…)

Target Market(s)

Mainly women (middle class probably with disposable incomes).

Industry/Entity Type

Massage

Contact Information for Business Card

Rosa Elwin Therapies, Tel: 07942 586113, email: vitalbloom@mailvane.com, (on back of card I want: Rosalind Elwin BScHons, OKQRB, GPCL.)

Requirements
Nice to have
• A logo for Rosa Elwin Therapies would be good.

```html
<!DOCTYPE html>
<html lang="en">
<head>
<meta charset="utf-8">
<title>Rosa Elwin Therapies – Business Card</title>
<link rel="stylesheet" href="https://fonts.googleapis.com/css2?family=Great+Vibes&family=Libre+Baskerville&display=swap">
<style>
  :root {
    --page-bg: #ece8e4;
    --purple-light: #b772c6;
    --purple-mid: #8e3ea0;
    --purple-deep: #5f1f72;
    --green-light: #5cae7e;
    --green-mid: #2b8a4d;
    --green-deep: #14612f;
    --icon-green: #2e9a5c;
    --ink-white: #ffffff;
    --card-shadow: rgba(40, 20, 10, 0.28);
  }
  * { margin: 0; padding: 0; box-sizing: border-box; }
  html, body { width: 1200px; height: 900px; overflow: hidden; }
  body { background: var(--page-bg); position: relative; }

  .card {
    position: absolute;
    width: 560px;
    height: 360px;
    border-radius: 4px;
    overflow: hidden;
    box-shadow: 0 14px 30px var(--card-shadow);
    color: var(--ink-white);
  }
  .card--front {
    left: 70px; top: 90px;
    background: linear-gradient(160deg, var(--purple-light) 0%, var(--purple-mid) 45%, var(--purple-deep) 100%);
  }
  .card--back {
    left: 570px; top: 450px;
    background: linear-gradient(160deg, var(--green-light) 0%, var(--green-mid) 45%, var(--green-deep) 100%);
  }

  .foliage {
    position: absolute;
    left: 0; bottom: 0;
    width: 100%; height: 100%;
  }

  .brand-name {
    position: absolute;
    left: 60px; top: 58px;
    font-family: "Great Vibes", cursive;
    font-size: 52px;
    line-height: 0.95;
    font-weight: 400;
  }
  .brand-name span { display: block; }
  .brand-name span + span { padding-left: 48px; }

  .contact {
    position: absolute;
    right: 34px; top: 88px;
    list-style: none;
    font-family: "Libre Baskerville", serif;
    font-size: 13px;
    text-align: right;
  }
  .contact li {
    display: flex;
    align-items: center;
    justify-content: flex-end;
    gap: 8px;
    margin-bottom: 9px;
  }
  .contact-icon { width: 16px; height: 16px; flex: none; }

  .holder {
    position: absolute;
    left: 250px; top: 95px;
    font-family: "Libre Baskerville", serif;
  }
  .holder-name {
    font-size: 16px;
    letter-spacing: 0.06em;
    text-transform: uppercase;
    font-weight: 400;
  }
  .holder-credentials {
    font-size: 15px;
    margin-top: 6px;
  }
</style>
</head>
<body>

<section class="card card--front" aria-label="Card front">
  <svg class="foliage" viewBox="0 0 560 360" preserveAspectRatio="none" role="img" aria-label="Scattered white leaf pattern along the lower edge">
    <defs>
      <linearGradient id="foliage-front" x1="0" y1="0" x2="0" y2="1">
        <stop offset="0" stop-color="#ffffff" stop-opacity="0.55"/>
        <stop offset="1" stop-color="#ffffff" stop-opacity="0.9"/>
      </linearGradient>
    </defs>
    <path d="M0 170 C60 160 110 200 150 250 C210 230 280 230 330 255 C390 235 450 215 520 195 L560 190 L560 360 L0 360 Z" fill="url(#foliage-front)"/>
  </svg>

  <h1 class="brand-name"><span>Rosa Elwin</span><span>Therapies</span></h1>

  <ul class="contact">
    <li>07942 586113
      <svg class="contact-icon" viewBox="0 0 16 16" aria-hidden="true">
        <circle cx="8" cy="8" r="8" fill="var(--icon-green)"/>
        <path d="M5 4.2 L6.6 4 L7.2 6 L6.3 6.8 C6.8 8 7.9 9.1 9.2 9.7 L10 8.8 L12 9.4 L11.8 11 C8 11.2 4.8 8 5 4.2 Z" fill="#fff"/>
      </svg>
    </li>
    <li>vitalbloom@mailvane.com
      <svg class="contact-icon" viewBox="0 0 16 16" aria-hidden="true">
        <circle cx="8" cy="8" r="8" fill="var(--icon-green)"/>
        <rect x="4" y="5.2" width="8" height="5.6" fill="#fff"/>
        <path d="M4 5.2 L8 8.4 L12 5.2" fill="none" stroke="var(--icon-green)" stroke-width="0.9"/>
      </svg>
    </li>
  </ul>
</section>

<section class="card card--back" aria-label="Card back">
  <svg class="foliage" viewBox="0 0 560 360" preserveAspectRatio="none" role="img" aria-label="Scattered white leaf pattern along the lower edge">
    <defs>
      <linearGradient id="foliage-back" x1="0" y1="0" x2="0" y2="1">
        <stop offset="0" stop-color="#ffffff" stop-opacity="0.5"/>
        <stop offset="1" stop-color="#ffffff" stop-opacity="0.88"/>
      </linearGradient>
    </defs>
    <path d="M0 150 C50 140 90 180 130 240 C200 225 270 230 330 250 C400 225 470 200 560 175 L560 360 L0 360 Z" fill="url(#foliage-back)"/>
  </svg>

  <div class="holder">
    <h2 class="holder-name">Rosalind Elwin</h2>
    <p class="holder-credentials">BScHons, OKQRB, GPCL</p>
  </div>
</section>

</body>
</html>
```